Healthcare Technology Company Business Card Design

Hi,

We require a new business card design thats catchy and professional.
Our target audience is healthcare professionals. See supplied artwork for our logo.

If you think its achievable please try add the tag line, not necessary however.
"Developing technologies to improve patient care and release operation benefits"

We'll require the following information on the card. No need to have the subject titles but i've referenced them for your convenience.

Personal Details
Mark Towler
Position: Director
Phone Number - 03 9471 5382
Mobile Number - 0427 836 259
Email: firstname.lastname@velkarin.com.au

Company Details
Suite 38, 216 Wendrell Street
Port Melbourne, Victoria
Fax: 03 8214 3975
velkarin.com.au

Prefer a thinner design than the normal stock standard business card dimensions.
Please ensure there is adequate bleed.

Target Market(s)

Healthcare Professionals

Industry/Entity Type

Healthcare

Font styles to use
Sans Serif

Requirements
Must have
• Clean, Sharp Looks
Should not have
• Any healthcare symbols

```html
<!DOCTYPE html>
<html lang="en">
<head>
<meta charset="utf-8">
<title>Velkarin Business Card</title>
<link rel="stylesheet" href="https://fonts.googleapis.com/css2?family=Barlow:wght@400;500;600&display=swap">
<style>
  :root {
    --stage: #e4e4e2;
    --card: #ffffff;
    --brand-blue: #3b6c96;
    --brand-navy: #33506d;
    --brand-orange: #f0962b;
    --ink: #4a4f55;
    --shadow: rgba(0, 0, 0, 0.14);
  }
  * { margin: 0; padding: 0; box-sizing: border-box; }
  html, body {
    width: 1200px;
    height: 716px;
    overflow: hidden;
    background: var(--stage);
    font-family: "Barlow", sans-serif;
  }
  .stage {
    width: 1200px;
    height: 716px;
    display: flex;
    align-items: center;
    justify-content: center;
    gap: 60px;
  }
  .card {
    position: relative;
    width: 520px;
    height: 290px;
    background: var(--card);
    border-radius: 6px;
    box-shadow: 0 6px 20px var(--shadow);
    overflow: hidden;
  }
  /* Front */
  .card--front {
    display: flex;
    align-items: center;
    justify-content: center;
  }
  .brand {
    display: flex;
    align-items: center;
    gap: 14px;
  }
  .brand__mark {
    width: 34px;
    height: 34px;
    background: var(--brand-orange);
  }
  .brand__name {
    font-size: 58px;
    font-weight: 600;
    color: var(--brand-blue);
    letter-spacing: -0.5px;
    line-height: 1;
  }
  /* Back */
  .details {
    position: absolute;
    left: 42px;
    top: 40px;
    color: var(--ink);
  }
  .person {
    display: flex;
    align-items: baseline;
    gap: 12px;
    margin-bottom: 6px;
  }
  .person__name {
    font-size: 22px;
    font-weight: 400;
    letter-spacing: 1px;
    color: var(--brand-navy);
  }
  .person__role {
    font-size: 15px;
    color: var(--brand-navy);
  }
  .contact-list {
    list-style: none;
    font-size: 13.5px;
    line-height: 1.3;
    margin-bottom: 10px;
  }
  .contact-list__label {
    display: inline-block;
    width: 14px;
    color: var(--brand-orange);
    font-weight: 500;
  }
  .email {
    font-size: 13.5px;
    margin-bottom: 12px;
  }
  .address {
    font-style: normal;
    font-size: 13.5px;
    line-height: 1.3;
    margin-bottom: 8px;
  }
  .website {
    font-size: 14px;
    font-weight: 600;
    color: var(--brand-blue);
  }
  .brand-corner {
    position: absolute;
    right: 34px;
    bottom: 30px;
    display: flex;
    align-items: center;
    gap: 10px;
  }
  .brand-corner .brand__mark {
    width: 22px;
    height: 22px;
  }
  .brand-corner .brand__name {
    font-size: 30px;
  }
</style>
</head>
<body>
  <main class="stage">
    <section class="card card--front" aria-label="Card front">
      <div class="brand">
        <span class="brand__mark"></span>
        <span class="brand__name">Velkarin</span>
      </div>
    </section>

    <section class="card card--back" aria-label="Card back">
      <div class="details">
        <div class="person">
          <span class="person__name">MARK TOWLER</span>
          <span class="person__role">Director</span>
        </div>
        <ul class="contact-list">
          <li><span class="contact-list__label">T</span>03 9471 5382</li>
          <li><span class="contact-list__label">M</span>0427 836 259</li>
          <li><span class="contact-list__label">F</span>03 8214 3975</li>
        </ul>
        <p class="email">firstname.lastname@velkarin.com.au</p>
        <address class="address">
          Suite 38, 216 Wendrell Street<br>
          Port Melbourne, Victoria
        </address>
        <p class="website">velkarin.com.au</p>
      </div>
      <div class="brand brand-corner">
        <span class="brand__mark"></span>
        <span class="brand__name">Velkarin</span>
      </div>
    </section>
  </main>
</body>
</html>
```